Gordon Pellbrook Consulting - Web Design Project

We need a web design for my new edgy consulting business specializing in innovation, technology and strategy.

It is our personal goal to turn each client into raving fans by helping them achieve their own business goals and aspirations through assisting them in raising their own innovation and marketing standards.

We provide our personalised and state-of-the-art services to our clients and boards who represent some of the world greatest innovative thinkers.
Updates

Here is some other information which may help shape your thinking.

I've had direct Involvement in the development of the following iPad, iPhone Applications and websites

FarbeyondOzlands.com (TerraLink platform) by Voyage Bureau
http://farbeyondozlands.example.au

Sail Verve by Bright Voyaging
https://apps.example-store.com/au/app/sail-verve/id100000001

uRedlandTR by Travel Territory Board
https://apps.example-store.com/au/app/uredlandtr/id100000002

Wexmoor Trips
http://www.wexmoortrips.example.au

Trek Mapper by Voyage Bureau
http://apps.example-store.com/au/app/trek-mapper/id100000003

Sunward by Sunward Travel Office
https://apps.example-store.com/au/app/sunward/id100000004

Upper Fernridge Valley Route by Visit Coastlands
https://apps.example-store.com/au/app/upper-fernridge-valley-route/id100000005

Wanderer Path by Travel Territory Board and Southern Plains Travel Council
https://apps.example-store.com/au/app/wanderers-path-grand-journey/id100000006

Gordon Pellbrook Consulting (GPC)
November 2012 – Present (8 months)Brisbane, Sydney, Canberra

Gordon’s consults to Small-to-Medium Enterprises (SME) and Government organisations on business strategy, technology strategy, risk mitigation, disruptive technology and innovation in the workplace.

Gordon’s consultancy mantra is that we cannot divorce economic life from cultural life particularly in an era when social capital may be as important as physical capital in business.

Reason: request from designers, I want to see their best efforts

Target Market(s)

35+

Industry/Entity Type

Business

Requirements
Must have
• Please use some of the personal image(s) contained in the zip files which can be downloaded from here

http://filedrop.example/k9Xq2Lm
http://filedrop.example/p4Rt7Vn
http://filedrop.example/z8Hw3Bc
Nice to have
• Black, Sleek design, maybe minimalist. Nice to have a Pixelle for the design. Nice to have it easily ported to Wordpress or be a modified Wordpress template. HTML 5, responsive design

```html
<!DOCTYPE html>
<html lang="en">
<head>
<meta charset="utf-8">
<title>Gordon Pellbrook Consulting</title>
<link rel="stylesheet" href="https://fonts.googleapis.com/css2?family=Open+Sans:wght@300;400;600&family=Arimo:wght@400;700&display=swap">
<style>
:root{
  --ink:#111;
  --dark:#1b1b1b;
  --darker:#0c0c0c;
  --brand-blue:#1e66b4;
  --hex-blue:#0d4a8c;
  --navy:#0f3f72;
  --text-blue:#1f5a97;
  --grey-text:#555;
  --line:#cfcfcf;
  --white:#fff;
}
*{box-sizing:border-box;margin:0;padding:0}
html,body{width:988px;height:1200px;overflow:hidden;background:var(--white)}
body{position:relative;font-family:"Open Sans",Arial,sans-serif;color:var(--ink)}
.abs{position:absolute}

/* top bar */
.topbar{left:0;top:0;width:988px;height:51px;background:linear-gradient(#202020,#050505)}
.topbar-rule{left:0;top:51px;width:988px;height:5px;background:linear-gradient(#2a7ad0,#124f93)}
.brand{left:155px;top:8px;color:var(--white);font-weight:300;font-size:26px;letter-spacing:-.3px}
.brand small{font-size:21px;font-weight:400}
.login-field{top:16px;width:96px;height:18px;background:#2c2c2c;border:1px solid #444;color:#777;font:10px Arimo,Arial,sans-serif;padding:2px 6px}
.login-btn{left:787px;top:16px;width:49px;height:18px;background:linear-gradient(#3a8ee0,#1a5fae);color:var(--white);font:700 9px Arimo,Arial,sans-serif;text-align:center;line-height:18px}

/* nav */
.navband{left:0;top:56px;width:988px;height:48px;background:linear-gradient(#f4f4f4,#e4e4e4 60%,#fff)}
.nav{left:292px;top:51px;display:flex;align-items:center;height:50px;list-style:none;font-size:16px}
.nav li{padding:0 12px;position:relative;color:#111}
.nav li+li::before{content:"";position:absolute;left:0;top:4px;height:13px;border-left:1px solid #aaa}
.nav li.current{background:linear-gradient(#3b3b3b,#151515);color:var(--white);height:50px;line-height:50px;padding:0 14px;margin-right:4px}
.nav li.current+li::before{display:none}

/* hero */
.map{left:285px;top:110px;width:580px;height:290px;background:radial-gradient(ellipse at 55% 45%,#e2e2e2,#f3f3f3 55%,rgba(255,255,255,0) 75%)}
.hero-dark{left:0;top:403px;width:988px;height:140px;background:linear-gradient(#2a2a2a,#141414)}
.portrait{left:150px;top:58px;width:145px;height:475px;background:linear-gradient(#2a2d33,#15171b 60%,#0c0d0f);border-radius:60px 60px 8px 8px}
.portrait-shadow{left:95px;top:300px;width:140px;height:130px;background:radial-gradient(ellipse,rgba(160,160,160,.45),rgba(160,160,160,0) 70%)}
.social{display:flex;gap:11px}
.diamond{width:18px;height:18px;transform:rotate(45deg);background:linear-gradient(#6a6a6a,#2b2b2b);border:2px solid #ddd;box-shadow:0 0 0 1px #777}
.hero-social{left:761px;top:114px}
.headline{right:152px;text-align:right;font-weight:300;white-space:nowrap}
.hl-1{top:160px;font-size:46px;color:#333;letter-spacing:-1px}
.hl-2{top:208px;font-size:57px;color:#111;letter-spacing:-2px}
.hl-3{top:262px;font-size:45px;color:var(--brand-blue);letter-spacing:-1px}
.service{width:140px;text-align:center}
.service svg{display:block;margin:0 auto}
.service p{color:#eee;font-weight:300;font-size:16px;line-height:16px;margin-top:4px}

/* intro */
.intro{left:170px;top:568px;width:648px;text-align:center;color:var(--text-blue);font-size:16.5px;line-height:28px}

/* clients */
.section-title{left:0;width:988px;top:683px;text-align:center;font-size:22px;font-weight:300;color:#111}
.section-title b{font-weight:600}
.arrow-btn{top:693px;width:22px;height:22px;border-radius:50%;border:1px solid #999;background:#fff}
.clients{left:181px;top:740px;display:flex;gap:18px}
.client{width:112px;height:100px;display:flex;align-items:center;justify-content:center;text-align:center;padding:8px;font-size:12px;font-weight:600;border:1px solid #555}
.client-1{background:#1a1c3a;color:#fff}
.client-2{background:#2a4fa8;color:#fff}
.client-3{background:linear-gradient(#7b828c,#2d3440);color:#fff}
.client-4{background:#f6dccb;color:#6a3a1e;border-color:#8a5a3a}
.client-5{background:#3f9ae0;color:#fff}

/* news + testimonials */
.col-title{top:885px;font-size:22px;font-weight:300;color:#111;letter-spacing:.3px}
.view-all{top:890px;width:63px;height:19px;border-radius:3px;background:var(--navy);color:#fff;font:10px Arimo,Arial,sans-serif;text-align:center;line-height:19px}
.news-item{left:181px;display:flex;gap:20px;font:11px/15px Arimo,Arial,sans-serif;color:#222}
.date{width:28px;height:30px;border:2px solid #333;border-top-width:5px;text-align:center;font:700 11px/13px Arimo,Arial,sans-serif;flex:none}
.date span{display:block;font-size:6px;line-height:6px}
.quote{left:529px;width:282px;height:68px;border:3px solid #ececec;border-radius:5px;padding:8px 10px;font:10px/15px Arimo,Arial,sans-serif;color:#333;background:#fff}
.quote::after{content:"";position:absolute;right:30px;bottom:-12px;border:9px solid transparent;border-top-color:#ececec;border-right:0}
.quote cite{display:block;margin-top:6px;font-style:normal;font-weight:700;color:#999;font-size:10px}

/* footer */
.footer{left:0;top:1120px;width:988px;height:53px;background:linear-gradient(#1e1e1e,#080808)}
.footer-links{left:181px;top:1129px;font:9px Arimo,Arial,sans-serif;color:#ccc;word-spacing:2px}
.footer-copy{left:181px;top:1148px;font:9px Arimo,Arial,sans-serif;color:#ccc}
.footer-social{left:497px;top:1137px}
.footer-brand{right:180px;top:1132px;color:#fff;font-weight:300;font-size:19px;letter-spacing:-.3px}
.footer-brand small{font-size:15px;font-weight:400}
</style>
</head>
<body>

<header>
  <div class="abs topbar"></div>
  <div class="abs topbar-rule"></div>
  <div class="abs brand">Gordon Pellbrook <small>Consulting</small></div>
  <div class="abs login-field" style="left:577px">Username</div>
  <div class="abs login-field" style="left:681px">Password</div>
  <div class="abs login-btn">LOGIN</div>
  <div class="abs navband"></div>
  <ul class="abs nav">
    <li class="current">HOME</li>
    <li>ABOUT</li>
    <li>SERVICES</li>
    <li>CONSULTANCY</li>
    <li>CONTACT US</li>
  </ul>
</header>

<section class="hero">
  <div class="abs map" role="img" aria-label="Dotted world map backdrop"></div>
  <div class="abs hero-dark"></div>
  <div class="abs portrait-shadow"></div>
  <div class="abs portrait" role="img" aria-label="Full-length portrait of Gordon Pellbrook in a dark suit"></div>

  <div class="abs social hero-social" aria-label="Social links">
    <span class="diamond"></span><span class="diamond"></span><span class="diamond"></span>
  </div>

  <div class="abs headline hl-1">you will definitely</div>
  <div class="abs headline hl-2">HAVE A GOOD START</div>
  <div class="abs headline hl-3">with us!</div>

  <div class="abs service" style="left:290px;top:332px">
    <svg width="128" height="138" viewBox="0 0 128 138">
      <polygon points="64,2 124,36 124,102 64,136 4,102 4,36" fill="#0d4a8c" stroke="#2a6cb3" stroke-width="2"/>
      <polyline points="36,50 36,96 96,96" fill="none" stroke="#fff" stroke-width="5"/>
      <polyline points="44,86 58,66 72,76 90,52" fill="none" stroke="#cfd6df" stroke-width="5"/>
      <polygon points="92,44 96,58 84,54" fill="#fff"/>
    </svg>
    <p>Organisational<br>Development</p>
  </div>
  <div class="abs service" style="left:431px;top:332px">
    <svg width="128" height="138" viewBox="0 0 128 138">
      <polygon points="64,2 124,36 124,102 64,136 4,102 4,36" fill="#0d4a8c" stroke="#2a6cb3" stroke-width="2"/>
      <circle cx="64" cy="70" r="26" fill="none" stroke="#fff" stroke-width="5"/>
      <circle cx="64" cy="44" r="11" fill="#dde3ea"/>
      <circle cx="41" cy="84" r="11" fill="#dde3ea"/>
      <circle cx="87" cy="84" r="11" fill="#dde3ea"/>
    </svg>
    <p>Audience<br>Development</p>
  </div>
  <div class="abs service" style="left:570px;top:332px">
    <svg width="128" height="138" viewBox="0 0 128 138">
      <polygon points="64,2 124,36 124,102 64,136 4,102 4,36" fill="#0d4a8c" stroke="#2a6cb3" stroke-width="2"/>
      <g fill="none" stroke="#fff" stroke-width="4">
        <circle cx="64" cy="69" r="30"/>
        <ellipse cx="64" cy="69" rx="13" ry="30"/>
        <line x1="34" y1="69" x2="94" y2="69"/>
        <line x1="38" y1="55" x2="90" y2="55"/>
        <line x1="38" y1="83" x2="90" y2="83"/>
      </g>
    </svg>
    <p>Insight<br>Research</p>
  </div>
  <div class="abs service" style="left:703px;top:332px">
    <svg width="128" height="138" viewBox="0 0 128 138">
      <polygon points="64,2 124,36 124,102 64,136 4,102 4,36" fill="#0d4a8c" stroke="#2a6cb3" stroke-width="2"/>
      <g fill="none" stroke="#e4e8ee" stroke-width="6">
        <circle cx="64" cy="69" r="30"/>
        <circle cx="64" cy="69" r="18"/>
      </g>
      <circle cx="64" cy="69" r="7" fill="#fff"/>
    </svg>
    <p>Evaluation</p>
  </div>
</section>

<p class="abs intro">Gordon’s consults to Small-to-Medium Enterprises (SME) and Government organisations on business strategy, technology strategy, risk mitigation, disruptive technology and innovation in the workplace.</p>

<section class="clients-section">
  <h2 class="abs section-title">OUR <b>VALUED CLIENTS</b></h2>
  <svg class="abs arrow-btn" style="left:170px" viewBox="0 0 22 22"><polyline points="13,6 8,11 13,16" fill="none" stroke="#222" stroke-width="2"/></svg>
  <svg class="abs arrow-btn" style="left:796px" viewBox="0 0 22 22"><polyline points="9,6 14,11 9,16" fill="none" stroke="#222" stroke-width="2"/></svg>
  <div class="abs clients">
    <div class="client client-1">FarbeyondOzlands</div>
    <div class="client client-2">Sail Verve</div>
    <div class="client client-3">uRedlandTR</div>
    <div class="client client-4">Wexmoor Trips</div>
    <div class="client client-5">Sunward</div>
  </div>
</section>

<section class="news">
  <svg class="abs" style="left:180px;top:880px" width="38" height="36" viewBox="0 0 38 36">
    <rect x="2" y="2" width="34" height="32" rx="3" fill="none" stroke="#1f4f86" stroke-width="2.5"/>
    <rect x="7" y="8" width="9" height="9" fill="#1f4f86"/>
    <g stroke="#1f4f86" stroke-width="2"><line x1="19" y1="9" x2="31" y2="9"/><line x1="19" y1="15" x2="31" y2="15"/><line x1="7" y1="21" x2="31" y2="21"/><line x1="7" y1="27" x2="31" y2="27"/></g>
  </svg>
  <h3 class="abs col-title" style="left:235px">NEWS / EVENT</h3>
  <div class="abs view-all" style="left:417px">View All</div>

  <div class="abs news-item" style="top:938px">
    <div class="date">20<span>FEB</span></div>
    <p style="width:225px">Lorem ipsum dolor sit amet, consectetuer adipiscing elit, sed diam nonummy nibh euismod tincidunt ut laoreet dolore magna.</p>
  </div>
  <div class="abs news-item" style="top:988px">
    <div class="date">20<span>FEB</span></div>
    <p style="width:265px">Lorem ipsum dolor sit amet, consectetuer adipiscing elit, sed diam nonummy nibh euismod tincidunt ut laoreet dolore magna.</p>
  </div>
  <div class="abs news-item" style="top:1034px">
    <div class="date">20<span>FEB</span></div>
    <p style="width:240px">Lorem ipsum dolor sit amet, consectetuer adipiscing elit, sed diam nonummy nibh euismod tincidunt ut laoreet dolore magna.</p>
  </div>
</section>

<section class="testimonials">
  <svg class="abs" style="left:524px;top:878px" width="36" height="38" viewBox="0 0 36 38">
    <g fill="none" stroke="#1f4f86" stroke-width="2.5">
      <polygon points="26,3 33,10 12,31 4,34 7,26"/>
      <line x1="22" y1="7" x2="29" y2="14"/>
    </g>
  </svg>
  <h3 class="abs col-title" style="left:569px">TESTIMONIALS</h3>
  <div class="abs view-all" style="left:748px">View All</div>

  <blockquote class="abs quote" style="top:925px">"Lorem ipsum dolor sit amet, consectetuer adipiscing elit, sed diam nonummy nibh euismod tincidunt ut laoreet dolore magna."<cite>— Martin Holloway</cite></blockquote>
  <blockquote class="abs quote" style="top:1009px">"Lorem ipsum dolor sit amet, consectetuer adipiscing elit, sed diam nonummy nibh euismod tincidunt ut laoreet dolore magna."<cite>— Martin Holloway</cite></blockquote>
</section>

<footer>
  <div class="abs footer"></div>
  <div class="abs footer-links">GPC &nbsp;|&nbsp; Recruitment &nbsp;|&nbsp; Press &nbsp;|&nbsp; Imprint &nbsp;|&nbsp; Contact Us</div>
  <div class="abs footer-copy">© 2013 Gordon Pellbrook Consulting All Rights Reserved.</div>
  <div class="abs social footer-social" aria-label="Social links">
    <span class="diamond"></span><span class="diamond"></span><span class="diamond"></span>
  </div>
  <div class="abs footer-brand">Gordon Pellbrook <small>Consulting</small></div>
</footer>

</body>
</html>
```